4 'Thank you' greetings cards designs

We are a small greetings card publisher and we need designs for a range of 'Thank you' greetings cards and notecards.
This project is for a total of 4 designs.
Please take a look at this board on Clipnest, to see the kind of thing we are looking for: https://www.pinboardly.example/marvk8150/gratitude-notes/
The cards will be printed at a maximum size of 131mm x 183mm (including a 3mm bleed) so please provide 300dpi CMYK files at this size. Please ensure that any text (or elements of the design that are not part of the bleed) are at least 11mm in from each edge. Also, please note that cards do not have to have a bleed if your design doesn't require it (e.g. a plain white background).
Please provide 2 designs in 'portrait' orientation and 2 in 'landscape'.
Please provide 2 designs that just have the words 'Thank you' and then 2 designs that include your choice of these alternative messages:
Thank you so much
Thanks very much
Thank you very much
Thanks a million
Just to say thank you
A big thank you
A really big thank you
Feel free to use an exclamation mark on a couple of your designs, if you wish!
Other than the above guidelines, everything else is up to you in terms of colours, fonts, shapes, etc. - but please use the Clipnest board to see the kind of designs we are looking for.
Thank you!

```html
<!DOCTYPE html>
<html lang="en">
<head>
<meta charset="utf-8">
<title>Thank you card</title>
<link rel="stylesheet" href="https://fonts.googleapis.com/css2?family=Caveat+Brush&display=swap">
<style>
  :root {
    --cream: #fffeee;
    --plum: #8e2a8f;
    --rose: #ee4f6f;
    --coral: #f4806a;
    --amber: #f8a531;
    --sun: #fbd65a;
    --violet: #7b4fa8;
    --crimson: #c8243f;
  }
  html, body {
    margin: 0;
    padding: 0;
    overflow: hidden;
  }
  .card {
    position: relative;
    width: 1200px;
    height: 859px;
    background: var(--cream);
    overflow: hidden;
  }
  .greeting {
    position: absolute;
    left: 0;
    right: 0;
    top: 250px;
    margin: 0;
    text-align: center;
    font-family: "Caveat Brush", cursive;
    font-weight: 400;
    font-size: 280px;
    line-height: 1;
    letter-spacing: 2px;
    color: var(--plum);
  }
  .bird {
    position: absolute;
    border-radius: 50%;
    opacity: 0.9;
  }
  .bird--pink    { background: linear-gradient(120deg, var(--rose), var(--coral)); }
  .bird--gold    { background: linear-gradient(120deg, var(--sun), var(--amber)); }
  .bird--violet  { background: linear-gradient(120deg, var(--violet), var(--rose)); }
  .bird--sunset  { background: linear-gradient(120deg, var(--sun), var(--coral)); }
  .bird--orange  { background: linear-gradient(120deg, var(--amber), var(--coral)); }
  .bird--crimson { background: linear-gradient(120deg, var(--coral), var(--crimson)); }

  .bird-1  { left: 66px;   top: 63px;  width: 275px; height: 153px; }
  .bird-2  { left: 416px;  top: 70px;  width: 91px;  height: 46px; }
  .bird-3  { left: 989px;  top: 25px;  width: 133px; height: 58px; }
  .bird-4  { left: 839px;  top: 83px;  width: 266px; height: 183px; }
  .bird-5  { left: 50px;   top: 424px; width: 100px; height: 71px; }
  .bird-6  { left: 1097px; top: 512px; width: 46px;  height: 41px; }
  .bird-7  { left: 103px;  top: 582px; width: 121px; height: 163px; }
  .bird-8  { left: 258px;  top: 745px; width: 74px;  height: 53px; }
  .bird-9  { left: 391px;  top: 640px; width: 78px;  height: 45px; }
  .bird-10 { left: 457px;  top: 565px; width: 249px; height: 233px; }
  .bird-11 { left: 889px;  top: 615px; width: 258px; height: 166px; }
</style>
</head>
<body>
  <main class="card">
    <div class="bird bird--pink bird-1" role="img" aria-label="Geometric pink and red dove in flight"></div>
    <div class="bird bird--gold bird-2" role="img" aria-label="Small yellow geometric bird in flight"></div>
    <div class="bird bird--violet bird-3" role="img" aria-label="Small purple and red geometric bird in flight"></div>
    <div class="bird bird--sunset bird-4" role="img" aria-label="Geometric yellow and coral dove with spread wings"></div>
    <div class="bird bird--orange bird-5" role="img" aria-label="Small orange geometric bird in flight"></div>
    <div class="bird bird--gold bird-6" role="img" aria-label="Tiny yellow geometric bird in flight"></div>
    <div class="bird bird--orange bird-7" role="img" aria-label="Orange geometric dove rising upward"></div>
    <div class="bird bird--gold bird-8" role="img" aria-label="Small yellow geometric bird in flight"></div>
    <div class="bird bird--crimson bird-9" role="img" aria-label="Small red geometric bird in flight"></div>
    <div class="bird bird--crimson bird-10" role="img" aria-label="Geometric pink and crimson dove in flight"></div>
    <div class="bird bird--pink bird-11" role="img" aria-label="Geometric coral and yellow dove with spread wings"></div>

    <h1 class="greeting">Thank you</h1>
  </main>
</body>
</html>
```